RLM Concreting and Excavation website design

We need a new webpage for our concreting business.

It just have the following pages
Home
Services
Galley
Online quote
FAQ
Contact

Examples are:
https://www.brookvalebuilders.example

Industry/Entity Type

Concreting

Font styles to use
Serif
Sans Serif

Colors
0054AA
0677BA
7BADD7
CADEEF
E8F1F8
0094D4
00A9DD
6FCCEA
C7EBF8
E9F6FB
59FF00
82FF00
B8FF75
E3FFCB
F4FFEA

Requirements
Should not have
• No shopping cart

```html
<!DOCTYPE html>
<html lang="en">
<head>
<meta charset="utf-8">
<title>RLM</title>
<link href="https://fonts.googleapis.com/css2?family=Baloo+2:wght@600;700;800&family=Montserrat:wght@500;600&family=Roboto:wght@400;500&display=swap" rel="stylesheet">
<style>
:root{
  --green:#8cc63f;
  --green-dark:#7ab52f;
  --blue:#0b4fa6;
  --blue-mid:#0779bf;
  --ink:#222;
  --text:#666;
  --white:#fff;
  --line:#e6e6e6;
}
*{margin:0;padding:0;box-sizing:border-box}
html,body{width:1200px;height:4292px;overflow:hidden}
body{position:relative;font-family:"Roboto",sans-serif;color:var(--ink);background:var(--white)}
.abs{position:absolute}
.heading{font-family:"Baloo 2",sans-serif;font-weight:800;color:var(--ink)}
.btn{position:absolute;background:var(--green);color:var(--white);border-radius:24px;font-family:"Montserrat",sans-serif;font-weight:600;font-size:13px;display:flex;align-items:center;justify-content:center;gap:5px;letter-spacing:.3px}
.photo{position:absolute}

/* top bar */
.topbar{left:0;top:0;width:1200px;height:42px;background:var(--green);color:var(--white);font-size:13px;display:flex;align-items:center;justify-content:center;font-family:"Montserrat",sans-serif;font-weight:500}

/* header */
.brand{left:60px;top:76px;display:flex;align-items:center;gap:14px}
.brand-mark{width:40px;height:40px;background:var(--green)}
.brand-name{font-family:"Baloo 2",sans-serif;font-weight:800;font-size:40px;line-height:48px;color:#333;letter-spacing:1px}
.nav{left:367px;top:92px;display:flex;gap:28px;font-family:"Montserrat",sans-serif;font-weight:600;font-size:13px;color:#333}
.nav .active{color:var(--green)}
.call{left:885px;top:80px;display:flex;align-items:center;gap:12px}
.call-icon{width:42px;height:42px;border-radius:50%;background:var(--green);display:flex;align-items:center;justify-content:center}
.call small{display:block;font-family:"Montserrat",sans-serif;font-size:13px;font-weight:500;color:#333}
.call strong{display:block;font-family:"Montserrat",sans-serif;font-size:19px;font-weight:500;color:#333}

/* hero */
.hero{left:0;top:167px;width:1200px;height:766px;background:linear-gradient(160deg,#8a8578 0%,#7b776c 40%,#a07a55 75%,#8d6a48 100%)}
.hero-shade{left:0;top:167px;width:1200px;height:766px;background:rgba(0,0,0,.18)}
.hero-title{left:0;top:435px;width:1200px;text-align:center;font-family:"Montserrat",sans-serif;font-weight:600;font-size:62px;color:var(--white);letter-spacing:1px}
.hero-sub{left:0;top:514px;width:1200px;text-align:center;font-family:"Montserrat",sans-serif;font-weight:600;font-size:27px;color:var(--white)}
.arrow-btn{width:45px;height:45px;border-radius:50%;background:#111;display:flex;align-items:center;justify-content:center}
.dots{left:565px;top:811px;display:flex;gap:6px}
.dots span{width:12px;height:12px;border-radius:50%;background:var(--white)}
.dots span.on{background:var(--green)}

/* services */
.section-title{left:0;width:1200px;text-align:center;font-size:38px}
.section-sub{left:0;width:1200px;text-align:center;font-size:14px;color:var(--text)}
.card{width:314px;height:505px;top:1103px;background:var(--white);box-shadow:0 2px 10px rgba(0,0,0,.15)}
.card .photo{left:0;top:0;width:314px;height:247px}
.card-icon{position:absolute;left:117px;top:200px;width:80px;height:80px;border-radius:50%;background:var(--white);box-shadow:0 2px 8px rgba(0,0,0,.2);display:flex;align-items:center;justify-content:center}
.card h3{position:absolute;left:0;top:298px;width:314px;text-align:center;font-family:"Roboto",sans-serif;font-weight:500;font-size:17px;line-height:26px;color:#222}
.card p{position:absolute;left:28px;top:358px;width:258px;text-align:center;font-size:13px;line-height:22px;color:var(--text)}
.card .btn{left:81px;top:434px;width:153px;height:43px}

/* gallery */
.gallery{left:0;top:1712px;width:1200px;height:788px;background:linear-gradient(100deg,#0779bf 0%,#3f9b96 45%,#8cc63f 100%)}
.gallery-title{left:0;top:1800px;width:1200px;text-align:center;font-size:38px;color:var(--white)}
.plus-circle{left:269px;top:2102px;width:64px;height:64px;border-radius:50%;background:rgba(255,255,255,.35);display:flex;align-items:center;justify-content:center}

/* quote */
.quote-title{left:112px;top:2590px;font-size:38px}
.quote-text{left:112px;top:2668px;width:455px;font-size:14.5px;line-height:25.8px;color:var(--text)}
.quote-tab{left:610px;top:2750px;width:118px;height:92px;background:var(--green);border-radius:0 46px 46px 0;display:flex;align-items:center;justify-content:flex-end;padding-right:10px}
.quote-tab span{width:70px;height:70px;border-radius:50%;border:4px solid var(--white);background:var(--green);display:flex;align-items:center;justify-content:center}

/* faq */
.faq-item{left:263px;width:669px;height:63px;background:var(--white);box-shadow:0 1px 8px rgba(0,0,0,.15);display:flex;align-items:center;padding-left:32px;font-family:"Baloo 2",sans-serif;font-weight:700;font-size:15px;color:#222}
.faq-plus{position:absolute;right:0;top:0;width:55px;height:63px;background:var(--green);color:var(--white);font-size:26px;display:flex;align-items:center;justify-content:center;font-family:"Roboto",sans-serif}

/* footer */
.footer-title{font-family:"Roboto",sans-serif;font-weight:500;font-size:18px;color:var(--white)}
.field{position:absolute;background:var(--white);font-size:13px;color:#777;padding:10px 18px}
.links{left:650px;top:3936px;list-style:none;color:var(--white);font-size:14px}
.links li{height:30px;display:flex;align-items:center;gap:10px}
.links li::before{content:"»";font-size:14px}
.contact{color:var(--white);font-size:14px;line-height:24px}
.social{width:32px;height:32px;border-radius:50%}
.divider{left:112px;top:4217px;width:976px;height:1px;background:rgba(255,255,255,.3)}
.copyright{left:0;top:4244px;width:1200px;text-align:center;color:var(--white);font-size:14px}
</style>
</head>
<body>

<div class="abs topbar">Lorem ipsum dolor sit amet, consectetur adipiscing elit, sed do eiusmod tempor</div>

<header>
  <div class="abs brand"><span class="brand-mark"></span><span class="brand-name">RLM</span></div>
  <nav class="abs nav">
    <span class="active">HOME</span><span>SERVICES</span><span>GALLERY</span><span>ONLINE QUOTE</span><span>FAQ</span><span>CONTACT</span>
  </nav>
  <div class="abs call">
    <span class="call-icon"><svg width="18" height="18" viewBox="0 0 24 24"><path fill="#fff" d="M6.6 10.8a15 15 0 0 0 6.6 6.6l2.2-2.2c.3-.3.7-.4 1-.2 1.1.4 2.3.6 3.6.6.6 0 1 .4 1 1V20c0 .6-.4 1-1 1A17 17 0 0 1 3 4c0-.6.4-1 1-1h3.5c.6 0 1 .4 1 1 0 1.3.2 2.5.6 3.6.1.3 0 .7-.2 1z"/></svg></span>
    <span><small>Call us Today :</small><strong>+1 888 888 8888</strong></span>
  </div>
</header>

<section>
  <div class="photo hero" role="img" aria-label="Aerial view of crew in hi-vis vests spreading wet concrete over steel mesh"></div>
  <div class="abs hero-shade"></div>
  <h1 class="abs hero-title">CONCRETING BUSINESS</h1>
  <p class="abs hero-sub">FREE ESTIMATES &nbsp;| GREAT CUSTOMER SERVICE &nbsp;| &nbsp;SINCE 2009</p>
  <span class="btn" style="left:524px;top:566px;width:153px;height:44px">GET STARTED</span>
  <span class="abs arrow-btn" style="left:36px;top:465px"><svg width="12" height="12" viewBox="0 0 12 12"><path d="M8 1 3 6l5 5" stroke="#fff" stroke-width="2" fill="none"/></svg></span>
  <span class="abs arrow-btn" style="left:1120px;top:465px"><svg width="12" height="12" viewBox="0 0 12 12"><path d="m4 1 5 5-5 5" stroke="#fff" stroke-width="2" fill="none"/></svg></span>
  <div class="abs dots"><span class="on"></span><span></span><span></span><span></span></div>
  <svg class="abs" style="left:0;top:826px" width="1200" height="110" viewBox="0 0 1200 110">
    <polygon points="0,2 592,107 0,107" fill="#fff"/>
    <polygon points="592,107 1200,10 1200,107" fill="#8cc63f"/>
    <polygon points="592,107 1200,60 1200,110 592,110" fill="#fff"/>
  </svg>
</section>

<section>
  <h2 class="abs heading section-title" style="top:1005px">OUR SERVICES</h2>
  <p class="abs section-sub" style="top:1063px">Lorem ipsum dolor sit amet, consectetur adipiscing elit, sed do eiusmod tempor</p>

  <article class="abs card" style="left:112px">
    <div class="photo" style="background:linear-gradient(180deg,#5f8fd1 0%,#8db3e0 45%,#6f7f55 75%,#4f6a36 100%)" role="img" aria-label="White tipper truck parked on grass"></div>
    <span class="card-icon"><svg width="40" height="32" viewBox="0 0 40 32" fill="none" stroke="#333" stroke-width="2"><rect x="2" y="6" width="22" height="16"/><path d="M24 12h8l6 6v4H24z"/><circle cx="10" cy="26" r="4"/><circle cx="30" cy="26" r="4"/></svg></span>
    <h3>Lorem ipsum dolor sit amet,<br>consectetur adipiscing</h3>
    <p>Lorem ipsum dolor sit amet, consectetur adipiscing elit, sed do eiusmod tempor incididunt ut labore et</p>
    <span class="btn">LEARN MORE <svg width="12" height="12" viewBox="0 0 12 12"><circle cx="6" cy="6" r="6" fill="#fff"/><path d="m5 3 3 3-3 3" stroke="#8cc63f" stroke-width="1.6" fill="none"/></svg></span>
  </article>

  <article class="abs card" style="left:443px">
    <div class="photo" style="background:linear-gradient(180deg,#8fb6df 0%,#9a5c45 40%,#5a4a3e 65%,#2d2d2f 100%)" role="img" aria-label="Brick house garage with new dark driveway"></div>
    <span class="card-icon"><svg width="36" height="34" viewBox="0 0 36 34" fill="none" stroke="#333" stroke-width="2"><path d="M3 16 18 3l15 13"/><path d="M7 13v18h22V13"/><rect x="14" y="20" width="8" height="11"/></svg></span>
    <h3>Lorem ipsum dolor sit amet,<br>consectetur adipiscing</h3>
    <p>Lorem ipsum dolor sit amet, consectetur adipiscing elit, sed do eiusmod tempor incididunt ut labore et</p>
    <span class="btn">LEARN MORE <svg width="12" height="12" viewBox="0 0 12 12"><circle cx="6" cy="6" r="6" fill="#fff"/><path d="m5 3 3 3-3 3" stroke="#8cc63f" stroke-width="1.6" fill="none"/></svg></span>
  </article>

  <article class="abs card" style="left:775px">
    <div class="photo" style="background:linear-gradient(180deg,#3d5a3a 0%,#586a5f 40%,#45505a 70%,#2f3a44 100%)" role="img" aria-label="Workers finishing a fresh concrete slab"></div>
    <span class="card-icon"><svg width="38" height="34" viewBox="0 0 38 34" fill="none" stroke="#333" stroke-width="2"><ellipse cx="20" cy="14" rx="12" ry="8"/><rect x="3" y="22" width="32" height="6"/><circle cx="10" cy="30" r="3"/><circle cx="28" cy="30" r="3"/></svg></span>
    <h3>Lorem ipsum dolor sit amet,<br>consectetur adipiscing</h3>
    <p>Lorem ipsum dolor sit amet, consectetur adipiscing elit, sed do eiusmod tempor incididunt ut labore et</p>
    <span class="btn">LEARN MORE <svg width="12" height="12" viewBox="0 0 12 12"><circle cx="6" cy="6" r="6" fill="#fff"/><path d="m5 3 3 3-3 3" stroke="#8cc63f" stroke-width="1.6" fill="none"/></svg></span>
  </article>
</section>

<section>
  <div class="abs gallery"></div>
  <h2 class="abs heading gallery-title">GALLERY</h2>
  <div class="photo" style="left:112px;top:1870px;width:378px;height:530px;background:linear-gradient(170deg,#6fa33a 0%,#8cc63f 50%,#7db338 100%)" role="img" aria-label="Steel reinforcement grid for a foundation slab"></div>
  <span class="abs plus-circle"><svg width="18" height="18" viewBox="0 0 18 18"><path d="M9 2v14M2 9h14" stroke="#333" stroke-width="3"/></svg></span>
  <div class="photo" style="left:502px;top:1870px;width:586px;height:258px;background:linear-gradient(180deg,#3f6fc4 0%,#7aa3dd 45%,#4f7a3a 75%,#35592a 100%)" role="img" aria-label="Tipper truck and trailer on grass"></div>
  <div class="photo" style="left:502px;top:2143px;width:286px;height:257px;background:linear-gradient(160deg,#4a4a4a 0%,#9a9a98 45%,#6a6a66 100%)" role="img" aria-label="Freshly poured concrete pathway"></div>
  <div class="photo" style="left:800px;top:2143px;width:288px;height:257px;background:linear-gradient(180deg,#7fb0e6 0%,#3f6336 45%,#a7a59e 80%,#bfbcb2 100%)" role="img" aria-label="Concrete footpath beside trees"></div>
</section>

<section>
  <h2 class="abs heading quote-title">ONLINE QUOTE</h2>
  <p class="abs quote-text">Lorem ipsum dolor sit amet, consectetur adipiscing elit, sed do eiusmod tempor incididunt ut labore et dolore magna aliqua. Ut enim ad minim veniam, quis nostrud exercitation ullamco laboris nisi ut aliquip ex ea commodo consequat. Duis aute irure dolor in reprehenderit in voluptate velit esse cillum dolore euLorem ipsum dolor sit amet, consectetur adipiscing elit, sed do eiusmod tempor incididunt ut labore et dolore magna aliqua. Ut enim ad minim veniam, quis nostrud exercitation ullamco laboris nisi ut aliquip ex ea commodo consequat. Duis aute irure dolor in reprehenderit in voluptate velit esse cillum dolore eu</p>
  <span class="btn" style="left:112px;top:2950px;width:153px;height:44px">LEARN MORE</span>
  <div class="photo" style="left:610px;top:2500px;width:590px;height:595px;background:linear-gradient(180deg,#9a9486 0%,#7d6b55 25%,#4d5054 55%,#3a3d42 85%,#a0583c 100%)" role="img" aria-label="House extension slab with plastic membrane and steel mesh ready to pour"></div>
  <span class="abs quote-tab"><span><svg width="34" height="34" viewBox="0 0 34 34"><circle cx="17" cy="17" r="15" fill="#fff"/><path d="M9 17h14M17 10l7 7-7 7" stroke="#8cc63f" stroke-width="3.5" fill="none"/></svg></span></span>
</section>

<section>
  <h2 class="abs heading section-title" style="top:3185px">FAQ</h2>
  <div class="abs faq-item" style="top:3252px">1.Lorem ipsum dolor sit amet, consectetur adipiscing elit ?<span class="faq-plus">+</span></div>
  <div class="abs faq-item" style="top:3333px">1.Lorem ipsum dolor sit amet, consectetur adipiscing elit ?<span class="faq-plus">+</span></div>
  <div class="abs faq-item" style="top:3422px">1.Lorem ipsum dolor sit amet, consectetur adipiscing elit ?<span class="faq-plus">+</span></div>
  <div class="abs faq-item" style="top:3503px">1.Lorem ipsum dolor sit amet, consectetur adipiscing elit ?<span class="faq-plus">+</span></div>
  <span class="btn" style="left:523px;top:3590px;width:154px;height:44px">VIEW MORE</span>
</section>

<footer>
  <svg class="abs" style="left:0;top:3730px" width="1200" height="562" viewBox="0 0 1200 562">
    <polygon points="0,50 600,8 0,95" fill="#8cc63f"/>
    <polygon points="0,95 600,8 1200,102 1200,562 0,562" fill="#0b4fa6"/>
  </svg>

  <h3 class="abs footer-title" style="left:112px;top:3895px">GET IN TOUCH</h3>
  <div class="field" style="left:112px;top:3943px;width:233px;height:39px">First Name</div>
  <div class="field" style="left:353px;top:3943px;width:235px;height:39px">Last Name</div>
  <div class="field" style="left:112px;top:3992px;width:233px;height:38px">Email</div>
  <div class="field" style="left:353px;top:3992px;width:235px;height:38px">Phone number</div>
  <div class="field" style="left:112px;top:4042px;width:476px;height:75px">Message</div>
  <span class="btn" style="left:112px;top:4135px;width:133px;height:43px;font-size:14px">SUBMIT</span>

  <h3 class="abs footer-title" style="left:650px;top:3895px">QUICK LINKS</h3>
  <ul class="abs links">
    <li>Home</li><li>Services</li><li>Gallery</li><li>Online quote</li><li>FAQ</li><li>Contact</li>
  </ul>

  <h3 class="abs footer-title" style="left:847px;top:3895px">CONTACT US</h3>
  <div class="abs contact" style="left:847px;top:3940px;display:flex;gap:12px">
    <svg width="14" height="18" viewBox="0 0 14 18" style="margin-top:4px"><path d="M7 0a7 7 0 0 0-7 7c0 5 7 11 7 11s7-6 7-11a7 7 0 0 0-7-7z" fill="#fff"/><circle cx="7" cy="7" r="2.5" fill="#0b4fa6"/></svg>
    <span>Lorem ipsum dolor sit amet,<br>consectetur adipis</span>
  </div>
  <div class="abs contact" style="left:849px;top:4021px;display:flex;gap:16px;align-items:center">
    <svg width="10" height="16" viewBox="0 0 10 16"><rect x="1" y="1" width="8" height="14" rx="1.5" fill="none" stroke="#fff" stroke-width="1.6"/><circle cx="5" cy="12.5" r="1" fill="#fff"/></svg>
    <span>+1 888 888 8888</span>
  </div>
  <div class="abs contact" style="left:847px;top:4061px;display:flex;gap:12px;align-items:center">
    <svg width="16" height="12" viewBox="0 0 16 12"><rect x="1" y="1" width="14" height="10" fill="none" stroke="#fff" stroke-width="1.5"/><path d="m1 1 7 6 7-6" stroke="#fff" stroke-width="1.5" fill="none"/></svg>
    <span>info@companyname.com</span>
  </div>

  <h3 class="abs footer-title" style="left:650px;top:4151px">STAY CONNECTED :</h3>
  <span class="abs social" style="left:850px;top:4149px;background:#3b5ba6"></span>
  <span class="abs social" style="left:888px;top:4149px;background:#d63b9b"></span>

  <div class="abs divider"></div>
  <p class="abs copyright">© 2021 Company Name &nbsp;| All Rights Reserved | Terms and Conditions</p>
</footer>

</body>
</html>
```